Brisk Framing website

I need a website for my construction. I want customers to see past builds and current projects Something that stands out and reflects awareness, safety, attention to details. I already have a logo designed by Pixel Harbor
Target Market(s)
Residential and Commercial sectors
Industry/Entity Type
Construction
Logo Text
Brisk Framing
Colors
EB3D1F
EC4F4E
F09395
F8D3D4
FCEDEE
Requirements
Must have
- My contact info
Nice to have
- Past projects

```html
<!DOCTYPE html>
<html lang="en">
<head>
<meta charset="utf-8">
<title>Brisk Framing</title>
<link href="https://fonts.googleapis.com/css2?family=Poppins:wght@400;500;600;700;800&family=Open+Sans:wght@400;600&display=swap" rel="stylesheet">
<style>
:root{
  --red:#EB3D1F;
  --red-soft:#EC4F4E;
  --pink:#F09395;
  --blush:#F8D3D4;
  --mist:#FCEDEE;
  --ink:#2b2b2b;
  --text:#6b6b6b;
  --grey-bg:#f3f3f5;
  --white:#ffffff;
}
*{margin:0;padding:0;box-sizing:border-box}
html,body{width:1200px;height:3660px;overflow:hidden}
body{position:relative;font-family:'Open Sans',Arial,sans-serif;color:var(--text);background:var(--white)}
h1,h2,h3,h4,.btn,.nav a,.logo{font-family:'Poppins',Arial,sans-serif}
.btn{display:inline-block;background:var(--red);color:var(--white);font-size:11px;font-weight:600;letter-spacing:.5px;padding:9px 22px;border-radius:20px;text-transform:uppercase;text-decoration:none}

/* header */
.site-header{position:absolute;top:0;left:0;width:1200px;height:88px;background:var(--white);display:flex;align-items:center;padding:0 60px;box-shadow:0 2px 6px rgba(0,0,0,.08);z-index:2}
.logo{display:flex;align-items:center;gap:10px;color:var(--red);font-weight:800;font-size:26px;letter-spacing:.5px;text-transform:uppercase}
.logo .mark{width:18px;height:18px;background:var(--red)}
.nav{display:flex;gap:36px;margin-left:auto;margin-right:40px}
.nav a{font-size:14px;color:var(--ink);text-decoration:none}
.nav a.active{color:var(--red)}
.header-phone{display:flex;align-items:center;gap:8px;background:var(--red);color:var(--white);font-family:'Poppins',sans-serif;font-size:14px;font-weight:600;padding:10px 20px;border-radius:24px}

/* hero */
.hero{position:absolute;top:88px;left:0;width:1200px;height:600px;background:linear-gradient(100deg,#6b4a33 0%,#4a3426 40%,#2a201b 75%,#1b1614 100%)}
.hero-copy{position:absolute;right:90px;top:150px;text-align:right}
.hero-copy h1{color:var(--white);font-size:50px;line-height:1.15;font-weight:800;text-transform:uppercase;margin-bottom:30px}
.hero-arrow{position:absolute;top:280px;width:30px;height:30px;border-radius:50%;background:var(--red);display:flex;align-items:center;justify-content:center}
.hero-arrow.prev{left:70px}.hero-arrow.next{right:60px}

/* contact strip */
.contact-strip{position:absolute;top:650px;left:200px;width:760px;height:70px}
.strip-call{position:absolute;left:0;top:0;width:400px;height:70px;background:var(--red);clip-path:polygon(4% 0,100% 0,96% 100%,0 100%);display:flex;align-items:center;justify-content:center;gap:12px;color:var(--white);font-family:'Poppins',sans-serif}
.strip-call small{font-size:14px;font-weight:500}
.strip-call strong{font-size:26px;font-weight:700}
.strip-mail{position:absolute;left:380px;top:0;width:380px;height:70px;background:#ececee;clip-path:polygon(4% 0,100% 0,96% 100%,0 100%);display:flex;align-items:center;padding-left:70px;gap:14px;color:var(--ink);font-size:16px}

/* section heading */
.section-title{position:absolute;left:60px;width:1080px;display:flex;align-items:center;gap:24px}
.section-title::before,.section-title::after{content:"";flex:1;height:2px;background:var(--blush)}
.section-title h2{font-size:38px;font-weight:700;color:#555;text-transform:uppercase;white-space:nowrap}
.section-title h2 span{color:var(--red)}

/* welcome */
.welcome-text{position:absolute;top:890px;left:250px;width:700px;text-align:center;font-size:13px;line-height:1.7}
.welcome-cta{position:absolute;top:965px;left:0;width:1200px;text-align:center}

/* services */
.services{position:absolute;top:1110px;left:0;width:1200px;height:1000px;background:var(--grey-bg)}
.service{position:absolute;left:60px;width:1080px;height:320px;display:flex}
.service .photo{width:540px;height:320px}
.service .body{width:540px;height:320px;background:var(--mist);padding:40px 34px}
.service h3{color:var(--red);font-size:30px;font-weight:600;margin-bottom:14px}
.service p{font-size:13px;line-height:1.75;margin-bottom:22px}

/* projects */
.projects{position:absolute;top:2280px;left:60px;width:1080px;display:flex;gap:27px}
.project-card{width:342px;height:430px;background:var(--grey-bg);box-shadow:0 2px 6px rgba(0,0,0,.06)}
.project-card .photo{height:220px}
.project-card .body{padding:24px 22px}
.project-card h4{font-size:17px;font-weight:600;color:var(--ink);line-height:1.45;margin-bottom:12px}
.project-card p{font-size:13px;line-height:1.7}

/* clients */
.clients{position:absolute;top:2800px;left:0;width:1200px;height:500px;background:var(--grey-bg)}
.client-list{position:absolute;top:180px;left:60px;width:1080px;display:flex;gap:40px}
.client-card{position:relative;width:240px;height:240px;background:var(--white);padding:50px 24px 20px}
.client-card .avatar{position:absolute;top:-28px;left:24px;width:64px;height:64px;border-radius:50%;background:linear-gradient(135deg,#c9a48c,#6b4f42)}
.client-card h4{font-size:13px;font-weight:600;color:var(--ink);margin-bottom:6px}
.stars{display:flex;gap:3px;margin-bottom:12px}
.client-card p{font-size:12px;line-height:1.7}

/* footer */
.site-footer{position:absolute;top:3420px;left:0;width:1200px;height:240px;background:var(--red);color:var(--white);padding:50px 60px}
.site-footer .logo{color:var(--white)}
.site-footer .logo .mark{background:var(--white)}
.footer-about{position:absolute;left:60px;top:110px;width:220px;font-size:12px;line-height:1.6;color:#ffe6e2}
.footer-links{position:absolute;left:340px;top:50px;list-style:none;font-size:13px;line-height:1.9}
.footer-contact{position:absolute;left:540px;top:50px;list-style:none;font-size:14px}
.footer-contact li{display:flex;gap:14px;align-items:flex-start;margin-bottom:18px;max-width:280px;line-height:1.5}
.footer-subscribe{position:absolute;left:900px;top:50px;width:240px;font-size:12px;line-height:1.6}
.footer-subscribe .field{margin-top:16px;height:38px;border:1px solid rgba(255,255,255,.7);border-radius:20px;padding:0 16px;display:flex;align-items:center;color:#ffe0da;font-size:12px}
.footer-subscribe .send{margin-top:12px;display:inline-block;background:var(--white);color:var(--red);font-family:'Poppins',sans-serif;font-weight:600;font-size:12px;padding:9px 26px;border-radius:20px}
</style>
</head>
<body>

<header class="site-header">
  <div class="logo"><span class="mark"></span>Brisk Framing</div>
  <nav class="nav">
    <a class="active" href="#">Home</a><a href="#">About</a><a href="#">Services</a><a href="#">Projects</a><a href="#">Testimonials</a><a href="#">Contact</a>
  </nav>
  <div class="header-phone">
    <svg width="14" height="14" viewBox="0 0 24 24" fill="#fff"><path d="M6.6 10.8a15 15 0 0 0 6.6 6.6l2.2-2.2a1 1 0 0 1 1-.25 11.4 11.4 0 0 0 3.6.57 1 1 0 0 1 1 1V20a1 1 0 0 1-1 1A17 17 0 0 1 3 4a1 1 0 0 1 1-1h3.5a1 1 0 0 1 1 1c0 1.25.2 2.45.57 3.57a1 1 0 0 1-.25 1z"/></svg>
    123 456 789
  </div>
</header>

<section class="hero" role="img" aria-label="Photo of a construction worker in a hard hat drilling on a building site">
  <div class="hero-arrow prev"><svg width="10" height="10" viewBox="0 0 10 10"><path d="M7 1 3 5l4 4" stroke="#fff" stroke-width="2" fill="none"/></svg></div>
  <div class="hero-arrow next"><svg width="10" height="10" viewBox="0 0 10 10"><path d="M3 1l4 4-4 4" stroke="#fff" stroke-width="2" fill="none"/></svg></div>
  <div class="hero-copy">
    <h1>We will build<br>your dream<br>in visual</h1>
    <a class="btn" href="#">Learn more</a>
  </div>
</section>

<div class="contact-strip">
  <div class="strip-call"><small>CALL US</small>
    <svg width="22" height="22" viewBox="0 0 24 24" fill="#fff"><path d="M6.6 10.8a15 15 0 0 0 6.6 6.6l2.2-2.2a1 1 0 0 1 1-.25 11.4 11.4 0 0 0 3.6.57 1 1 0 0 1 1 1V20a1 1 0 0 1-1 1A17 17 0 0 1 3 4a1 1 0 0 1 1-1h3.5a1 1 0 0 1 1 1c0 1.25.2 2.45.57 3.57a1 1 0 0 1-.25 1z"/></svg>
    <strong>123 456 7890</strong></div>
  <div class="strip-mail">
    <svg width="24" height="18" viewBox="0 0 24 18"><rect x="1" y="1" width="22" height="16" rx="2" fill="none" stroke="#333" stroke-width="2"/><path d="M1 2l11 8 11-8" fill="none" stroke="#333" stroke-width="2"/></svg>
    info@briskframing.com
  </div>
</div>

<div class="section-title" style="top:825px"><h2>Welcome to <span>Brisk Framing</span></h2></div>
<p class="welcome-text">Lorem Ipsum has been the industry's standard dummy text ever since the 1500s, when an unknown printer took a galley of type and scrambled it to make a type specimen book. It has survived not only five centuries but also the leap into electronic typesetting, remaining essentially unchanged.</p>
<div class="welcome-cta"><a class="btn" href="#">Read more</a></div>

<section class="services">
  <div class="service" style="top:10px">
    <div class="photo" role="img" aria-label="Photo of a modern two-storey house with a garage at dusk" style="background:linear-gradient(180deg,#5d7fae 0%,#9fb7d6 45%,#6e6a66 75%,#4b4f47 100%)"></div>
    <div class="body"><h3>Residential Construction</h3>
      <p>Lorem ipsum dolor sit amet, consectetur adipiscing elit. Praesent elit diam, malesuada sit amet felis ac, blandit eleifend urna. Integer consequat magna scelerisque aliquet aliquam. Etiam et malesuada enim. Mauris non volutpat lectus, efficitur fermentum urna.</p>
      <a class="btn" href="#">Read more</a></div>
  </div>
  <div class="service" style="top:340px">
    <div class="body"><h3>Commercial Construction</h3>
      <p>Lorem ipsum dolor sit amet, consectetur adipiscing elit. Praesent elit diam, malesuada sit amet felis ac, blandit eleifend urna. Integer consequat magna scelerisque aliquet aliquam. Etiam et malesuada enim. Mauris non volutpat lectus, efficitur fermentum urna.</p>
      <a class="btn" href="#">Read more</a></div>
    <div class="photo" role="img" aria-label="Photo of a glass-fronted commercial building with trees and a paved walkway" style="background:linear-gradient(160deg,#a9c4dc 0%,#7b8f7a 45%,#8a6048 70%,#b9b2a8 100%)"></div>
  </div>
  <div class="service" style="top:670px">
    <div class="photo" role="img" aria-label="Photo of engineers in hard hats and safety vests reviewing plans on site" style="background:linear-gradient(180deg,#cfd4d8 0%,#9aa0a3 40%,#b7c13a 70%,#3c3f40 100%)"></div>
    <div class="body"><h3>Development</h3>
      <p>Lorem ipsum dolor sit amet, consectetur adipiscing elit. Praesent elit diam, malesuada sit amet felis ac, blandit eleifend urna. Integer consequat magna scelerisque aliquet aliquam. Etiam et malesuada enim. Mauris non volutpat lectus.</p>
      <a class="btn" href="#">Read more</a></div>
  </div>
</section>

<div class="section-title" style="top:2195px"><h2>Recent <span>Project</span></h2></div>
<section class="projects">
  <article class="project-card">
    <div class="photo" role="img" aria-label="Photo of a large modern building under an overcast sky" style="background:linear-gradient(180deg,#9aa6b0 0%,#6d6a64 60%,#4c4a46 100%)"></div>
    <div class="body"><h4>Lorem Ipsum is simply dummy text of the printing</h4><p>Lorem Ipsum is simply dummy text of the printing and typesetting industry. Lorem Ipsum has been the industry's standard dummy.</p></div>
  </article>
  <article class="project-card">
    <div class="photo" role="img" aria-label="Photo of a bright modern interior with large windows" style="background:linear-gradient(180deg,#2f2f31 0%,#8d9499 50%,#d2d4d2 100%)"></div>
    <div class="body"><h4>Lorem Ipsum is simply dummy text of the printing</h4><p>Lorem Ipsum is simply dummy text of the printing and typesetting industry. Lorem Ipsum has been the industry's standard dummy.</p></div>
  </article>
  <article class="project-card">
    <div class="photo" role="img" aria-label="Photo of a white house with red roofs surrounded by trees" style="background:linear-gradient(180deg,#cfe0ee 0%,#c4574a 45%,#e9e7e2 70%,#6b8a4e 100%)"></div>
    <div class="body"><h4>Lorem Ipsum is simply dummy text of the printing</h4><p>Lorem Ipsum is simply dummy text of the printing and typesetting industry. Lorem Ipsum has been the industry's standard dummy.</p></div>
  </article>
</section>

<section class="clients">
  <div class="section-title" style="top:110px"><h2>Our <span>Happy Clients</span></h2></div>
  <div class="client-list">
    <div class="client-card"><div class="avatar" role="img" aria-label="Client portrait photo"></div><h4>MARA</h4>
      <div class="stars"><svg width="90" height="14" viewBox="0 0 90 14"><g fill="#f5b400"><path id="s" d="M7 0l2 4.6 5 .5-3.8 3.3 1.1 5L7 10.8 2.7 13.4l1.1-5L0 5.1l5-.5z"/><use href="#s" x="18"/><use href="#s" x="36"/><use href="#s" x="54"/><use href="#s" x="72"/></g></svg></div>
      <p>Lorem ipsum dolor sit amet, consectetur adipiscing elit, sed do eiusmod tempor incididunt ut labore et dolore magna aliqua.</p></div>
    <div class="client-card"><div class="avatar" role="img" aria-label="Client portrait photo" style="background:linear-gradient(135deg,#d9c2b0,#5a4a40)"></div><h4>MARA</h4>
      <div class="stars"><svg width="90" height="14" viewBox="0 0 90 14"><g fill="#f5b400"><use href="#s"/><use href="#s" x="18"/><use href="#s" x="36"/><use href="#s" x="54"/><use href="#s" x="72"/></g></svg></div>
      <p>Lorem ipsum dolor sit amet, consectetur adipiscing elit, sed do eiusmod tempor incididunt ut labore et dolore magna aliqua.</p></div>
    <div class="client-card"><div class="avatar" role="img" aria-label="Client portrait photo" style="background:linear-gradient(135deg,#c7a07e,#3f3a36)"></div><h4>MARA</h4>
      <div class="stars"><svg width="90" height="14" viewBox="0 0 90 14"><g fill="#f5b400"><use href="#s"/><use href="#s" x="18"/><use href="#s" x="36"/><use href="#s" x="54"/><use href="#s" x="72"/></g></svg></div>
      <p>Lorem ipsum dolor sit amet, consectetur adipiscing elit, sed do eiusmod tempor incididunt ut labore et dolore magna aliqua.</p></div>
    <div class="client-card"><div class="avatar" role="img" aria-label="Client portrait photo" style="background:linear-gradient(135deg,#b9a393,#4a4441)"></div><h4>MARA</h4>
      <div class="stars"><svg width="90" height="14" viewBox="0 0 90 14"><g fill="#f5b400"><use href="#s"/><use href="#s" x="18"/><use href="#s" x="36"/><use href="#s" x="54"/><use href="#s" x="72"/></g></svg></div>
      <p>Lorem ipsum dolor sit amet, consectetur adipiscing elit, sed do eiusmod tempor incididunt ut labore et dolore magna aliqua.</p></div>
  </div>
</section>

<footer class="site-footer">
  <div class="logo"><span class="mark"></span>Brisk Framing</div>
  <p class="footer-about">Lorem ipsum dolor sit amet, consectetur adipiscing elit, sed do eiusmod tempor.</p>
  <ul class="footer-links"><li>Home</li><li>About</li><li>Services</li><li>Projects</li><li>Testimonials</li><li>Contact</li></ul>
  <ul class="footer-contact">
    <li><svg width="16" height="20" viewBox="0 0 16 20" fill="#fff"><path d="M8 0a8 8 0 0 0-8 8c0 6 8 12 8 12s8-6 8-12a8 8 0 0 0-8-8zm0 11a3 3 0 1 1 0-6 3 3 0 0 1 0 6z"/></svg>Lorem Ipsum is simply dummy text of the printing.</li>
    <li><svg width="16" height="16" viewBox="0 0 24 24" fill="#fff"><path d="M6.6 10.8a15 15 0 0 0 6.6 6.6l2.2-2.2a1 1 0 0 1 1-.25 11.4 11.4 0 0 0 3.6.57 1 1 0 0 1 1 1V20a1 1 0 0 1-1 1A17 17 0 0 1 3 4a1 1 0 0 1 1-1h3.5a1 1 0 0 1 1 1c0 1.25.2 2.45.57 3.57a1 1 0 0 1-.25 1z"/></svg>123 456 7890</li>
    <li><svg width="18" height="14" viewBox="0 0 24 18"><rect x="1" y="1" width="22" height="16" rx="2" fill="none" stroke="#fff" stroke-width="2"/><path d="M1 2l11 8 11-8" fill="none" stroke="#fff" stroke-width="2"/></svg>info@briskframing.com</li>
  </ul>
  <div class="footer-subscribe">
    <p>Subscribe to stay with us and get our latest news and updates.</p>
    <div class="field">Enter Your Email</div>
    <span class="send">Subscribe Now</span>
  </div>
</footer>

</body>
</html>
```